VENTO SAURELLE

Project name: “Vento Saurelle” website
Objective: To create an elegant website,
intuitive and responsive to present this
what is “Vento Saurelle”
See attached specifications.

```html
<!DOCTYPE html>
<html lang="en">
<head>
<meta charset="utf-8">
<title>Vento Saurelle</title>
<link href="https://fonts.googleapis.com/css2?family=Merriweather:wght@700;900&family=Montserrat:wght@400;500;600;700&display=swap" rel="stylesheet">
<style>
:root{
  --green:#3a573b;
  --green-text:#3c5e3d;
  --sage:#a3b3a3;
  --white:#ffffff;
  --card:#f7f7f7;
  --ink:#1e1e1e;
  --link:#4d6a4d;
  --badge:#1f3f8a;
}
*{box-sizing:border-box;margin:0;padding:0}
html,body{width:1200px;height:2846px;overflow:hidden}
body{position:relative;background:var(--white);font-family:"Montserrat",sans-serif;color:var(--ink)}
.abs{position:absolute}
.serif{font-family:"Merriweather",serif;font-weight:700}

/* nav */
.site-nav{left:0;top:0;width:1200px;height:49px;background:var(--white);border-bottom:1px solid #ddd;z-index:3}
.site-nav a{position:absolute;top:16px;font-size:15px;color:var(--green-text);text-decoration:none}
.brand-badge{left:490px;top:-59px;width:220px;height:220px;border-radius:50%;background:var(--green);z-index:4;display:flex;align-items:flex-end;justify-content:center;padding-bottom:56px}
.brand-badge span{color:var(--white);font-weight:700;font-size:15px;letter-spacing:1.5px}

/* hero */
.hero{left:0;top:49px;width:1200px;height:608px;background:linear-gradient(160deg,#6f8f4c 0%,#4c6e35 40%,#5d7d3f 70%,#3f5d2d 100%)}
.hero-dots{left:176px;top:300px}
.hero-dots i{display:block;width:9px;height:9px;border-radius:50%;background:#c9d1c4;margin-bottom:16px}
.hero-title{left:0;width:1200px;top:360px;text-align:center;font-size:72px;color:var(--white)}
.hero-sub{left:280px;width:640px;top:448px;text-align:center;font-size:16.5px;font-weight:500;line-height:20px;color:var(--white)}
.btn{display:flex;align-items:center;justify-content:center;background:var(--sage);color:var(--green-text);font-weight:700;border-radius:30px}
.hero-btn{left:494px;top:520px;width:213px;height:51px;font-size:18px}

/* welcome */
.h2{left:0;width:1200px;text-align:center;color:var(--green-text);font-size:46px}
.welcome-title{top:700px}
.welcome-sub{left:0;width:1200px;top:760px;text-align:center;font-weight:700;font-size:16px}
.welcome-text{left:200px;width:800px;text-align:center;font-size:13.3px;line-height:24px}
.read-btn{left:541px;top:971px;width:120px;height:39px;font-size:14.5px}

/* activities */
.activities-title{top:1072px}
.activity-band{left:0;top:1355px;width:1200px;height:308px;background:var(--sage)}
.activity-card{width:292px;height:382px;background:var(--card);border-radius:8px;padding:7px}
.activity-card .photo{width:278px;height:310px}
.activity-card h3{text-align:center;color:var(--green-text);font-size:21px;font-weight:700;margin-top:22px}
.arrow{width:16px;height:16px}

/* feed */
.feed-title{top:1706px}
.feed-card{top:1787px;width:222px;height:293px;background:var(--card);border-radius:8px;padding:9px}
.feed-card .photo{width:204px;height:128px}
.feed-card .badge{position:absolute;left:97px;top:124px;width:28px;height:28px;border-radius:50%;background:var(--badge)}
.feed-card p{margin-top:20px;padding:0 8px;text-align:center;font-size:11.5px;line-height:15px;color:#333}

/* testimonial */
.testimonial{left:0;top:2123px;width:1200px;height:381px;background:var(--green)}
.avatar{left:560px;top:2208px;width:80px;height:80px;border-radius:50%;background:linear-gradient(160deg,#d9d6d2,#9e8c80)}
.review-mark{left:615px;top:2250px;width:32px;height:32px;border-radius:50%;background:var(--white)}
.quote{left:215px;width:770px;top:2303px;text-align:center;color:var(--white);font-size:15px;line-height:20px}

/* footer */
.site-footer{left:0;top:2504px;width:1200px;height:342px;background:var(--sage)}
.footer-badge{left:110px;top:2539px;width:174px;height:174px;border-radius:50%;background:var(--green);display:flex;align-items:center;justify-content:center}
.footer-badge span{color:var(--white);font-weight:700;font-size:15px;letter-spacing:1.5px;margin-top:56px}
.footer-head{top:2555px;font-size:20px;font-weight:700;color:var(--green-text);border-left:3px solid var(--green-text);padding-left:14px;line-height:24px}
.footer-list{font-size:13px;color:var(--link);line-height:15px}
.social{top:2617px;width:36px;height:36px;border-radius:50%;background:var(--green)}
.footer-rule{left:0;top:2770px;width:1200px;height:1px;background:#7f907f}
.copyright{left:0;width:1200px;top:2797px;text-align:center;font-size:13px;color:var(--link)}
</style>
</head>
<body>

<header>
  <nav class="site-nav abs">
    <a style="left:163px">Home</a>
    <a style="left:242px">About Us</a>
    <a style="left:343px">How we help?</a>
    <a style="left:743px">Land Prospecting</a>
    <a style="left:905px">Contact Us</a>
  </nav>
  <div class="brand-badge abs"><span>VENTO SAURELLE</span></div>
</header>

<section class="hero abs" role="img" aria-label="Aerial view of rolling green fields, hedgerows and a farmhouse in the countryside"></section>
<div class="hero-dots abs"><i></i><i></i><i></i><i></i></div>
<h1 class="hero-title abs serif">Vento Saurelle</h1>
<p class="hero-sub abs">Welcome to the heart of France—Limousin, a region renowned for its rolling green landscapes, rich rural heritage, and unmatched quality of life.</p>
<a class="hero-btn abs btn">Request a Quote</a>

<section>
  <h2 class="welcome-title h2 abs serif">Welcome To Vento Saurelle</h2>
  <p class="welcome-sub abs">Your Gateway to Land, Nature, and New Possibilities</p>
  <p class="welcome-text abs" style="top:807px">Welcome to the heart of France—Limousin, a region renowned for its rolling green landscapes, rich rural heritage, and unmatched quality of life. Whether you're searching for agricultural land, woodland, development plots, or a rural retreat, Limousin offers space, opportunity, and authenticity.</p>
  <p class="welcome-text abs" style="top:903px">Our platform brings together landowners, buyers, investors, and professionals, creating a trusted place to connect, explore opportunities, and build your future in one of France's most beautiful natural regions.</p>
  <a class="read-btn abs btn">Read more</a>
</section>

<section>
  <h2 class="activities-title h2 abs serif">Activities to do in Limousin</h2>
  <div class="activity-band abs"></div>
  <svg class="arrow abs" style="left:66px;top:1317px" viewBox="0 0 16 16"><path d="M11 2 5 8l6 6" fill="none" stroke="#222" stroke-width="2"/></svg>
  <svg class="arrow abs" style="left:1113px;top:1338px" viewBox="0 0 16 16"><path d="M5 2l6 6-6 6" fill="none" stroke="#222" stroke-width="2"/></svg>
  <article class="activity-card abs" style="left:141px;top:1188px">
    <div class="photo" role="img" aria-label="Stone bridge reflected in a calm river with autumn trees" style="background:linear-gradient(180deg,#b9b5aa 0%,#8a6f3a 40%,#6b5a32 65%,#3f5a2a 100%)"></div>
    <h3>Nature walks</h3>
  </article>
  <article class="activity-card abs" style="left:454px;top:1159px">
    <div class="photo" role="img" aria-label="Old town street with timber houses and colourful hanging decorations" style="background:linear-gradient(180deg,#7f8fb0 0%,#8c6f5c 45%,#a4968a 75%,#6f6a62 100%)"></div>
    <h3>Cultural visits</h3>
  </article>
  <article class="activity-card abs" style="left:767px;top:1188px">
    <div class="photo" role="img" aria-label="Paddleboarding on a tree-lined river" style="background:linear-gradient(180deg,#6f8f4a 0%,#3f5a2c 45%,#2f4a3c 75%,#1f2e2c 100%)"></div>
    <h3>Family outings</h3>
  </article>
</section>

<section>
  <h2 class="feed-title h2 abs serif">Community Feed</h2>
  <svg class="arrow abs" style="left:86px;top:1916px" viewBox="0 0 16 16"><path d="M11 2 5 8l6 6" fill="none" stroke="#222" stroke-width="2"/></svg>
  <svg class="arrow abs" style="left:1097px;top:1919px" viewBox="0 0 16 16"><path d="M5 2l6 6-6 6" fill="none" stroke="#222" stroke-width="2"/></svg>
  <article class="feed-card abs" style="left:140px">
    <div class="photo" role="img" aria-label="Country path through a summer meadow" style="background:linear-gradient(180deg,#a9c6e4 0%,#5f8a3c 45%,#b7a55c 100%)"></div>
    <span class="badge"></span>
    <p>Lorem ipsum dolor sit amet, consectetur adipiscing elit, sed do eiusmod tempor incididunt ut labore et dolore magna aliqua. Quis ipsum suspendisse ultrices gravida. Risus commodo viverra maecenas accumsan lacus vel facilisis.</p>
  </article>
  <article class="feed-card abs" style="left:373px">
    <div class="photo" role="img" aria-label="Outdoor market stalls under autumn trees" style="background:linear-gradient(180deg,#c98a3a 0%,#9a4a32 50%,#6b4f3a 100%)"></div>
    <span class="badge"></span>
    <p>Lorem ipsum dolor sit amet, consectetur adipiscing elit, sed do eiusmod tempor incididunt ut labore et dolore magna aliqua. Quis ipsum suspendisse ultrices gravida. Risus commodo viverra maecenas accumsan lacus vel facilisis.</p>
  </article>
  <article class="feed-card abs" style="left:605px">
    <div class="photo" role="img" aria-label="Event tents set up on a green lawn" style="background:linear-gradient(180deg,#6fb6e8 0%,#8fc0d8 45%,#4f9a3a 100%)"></div>
    <span class="badge"></span>
    <p>Lorem ipsum dolor sit amet, consectetur adipiscing elit, sed do eiusmod tempor incididunt ut labore et dolore magna aliqua. Quis ipsum suspendisse ultrices gravida. Risus commodo viverra maecenas accumsan lacus vel facilisis.</p>
  </article>
  <article class="feed-card abs" style="left:838px">
    <div class="photo" role="img" aria-label="Aerial view of a marquee event in a field" style="background:linear-gradient(180deg,#4f6a34 0%,#8a9a6a 50%,#5f5a34 100%)"></div>
    <span class="badge"></span>
    <p>Lorem ipsum dolor sit amet, consectetur adipiscing elit, sed do eiusmod tempor incididunt ut labore et dolore magna aliqua. Quis ipsum suspendisse ultrices gravida. Risus commodo viverra maecenas accumsan lacus vel facilisis.</p>
  </article>
</section>

<section class="testimonial abs"></section>
<div class="avatar abs" role="img" aria-label="Portrait of the reviewer"></div>
<span class="review-mark abs"></span>
<svg class="arrow abs" style="left:96px;top:2318px" viewBox="0 0 16 16"><path d="M11 2 5 8l6 6" fill="none" stroke="#fff" stroke-width="2"/></svg>
<svg class="arrow abs" style="left:1106px;top:2321px" viewBox="0 0 16 16"><path d="M5 2l6 6-6 6" fill="none" stroke="#fff" stroke-width="2"/></svg>
<blockquote class="quote abs">“Lorem ipsum dolor sit amet, consectetur adipiscing elit, sed do eiusmod tempor incididunt ut labore et dolore magna aliqua. Quis ipsum suspendisse ultrices gravida. Risus commodo viverra maecenas accumsan lacus vel facilisis. “</blockquote>

<footer>
  <div class="site-footer abs"></div>
  <div class="footer-badge abs"><span>VENTO SAURELLE</span></div>
  <h4 class="footer-head abs" style="left:354px">Quick Links</h4>
  <ul class="footer-list abs" style="left:371px;top:2607px;list-style:none;line-height:24.5px">
    <li>Home</li><li>About Us</li><li>How &nbsp;we help?</li>
  </ul>
  <h4 class="footer-head abs" style="left:570px">Contact Us</h4>
  <p class="footer-list abs" style="left:575px;top:2607px">#123, Lorium ipsum,<br>Dolor amit,<br>City</p>
  <p class="footer-list abs" style="left:575px;top:2667px">1-800 555 014</p>
  <p class="footer-list abs" style="left:575px;top:2698px">info@ventosaurelle.com</p>
  <h4 class="footer-head abs" style="left:829px">Follow Us</h4>
  <span class="social abs" style="left:834px"></span>
  <span class="social abs" style="left:876px"></span>
  <span class="social abs" style="left:917px"></span>
  <div class="footer-rule abs"></div>
  <p class="copyright abs">Copyright © 2025, www.ventosaurelle.com</p>
</footer>

</body>
</html>
```